Business Card Professional Clean - Ledgerpeak

Create a business card for my company that deals with Cryptocurrencies. I have a few designs ideas that I'd like to be implemented. Thanks! I will include the logo files, and a link to the design styles that I like.

Target Market(s)

Professionals

Industry/Entity Type

Consulting

Contact Information for Business Card

Name: Mark Dunn
Title: CEO/Technical Director
Phone: (587)430-9158
E-mail: mdunn@ledgerpeak.example
Address: Suite 512, 208-3375 Harwood Lane NW

Twitter: @LedgerPeakYYC
Instagram: ledgerpeakyyc

Colors
92b5d7
3276b5
33a6d7
85acd3
85cae6
0592cd

Requirements
Must have
• Some colors that match with the logo and the pictures I put in below.
• Ideally the finished product would look something like the attachments showing the color gradient I want.
Nice to have
• Please see some of the attachments I've included. This is very close to the final product that I would like to see. If someone could recreate something like those I would definitely feel pretty good about it.
• For the instagram and twitter please use the symbols/icon to represent it on the card.
Should not have
• No crazy colors and unprofessional styles. I just want clear info. Don't go outside the boundaries of the colors in the attachment and we should be good. No crazy weird fonts either.

```html
<!DOCTYPE html>
<html lang="en">
<head>
<meta charset="utf-8">
<title>Ledgerpeak Business Card</title>
<link rel="stylesheet" href="https://fonts.googleapis.com/css2?family=Cinzel:wght@500&family=Open+Sans:wght@400;600;700&display=swap">
<style>
  :root {
    --backdrop: #2e2f31;
    --paper: #f2f2f2;
    --brand-blue: #0b4e98;
    --slate: #3c4552;
    --divider: #ffffff;
    --ink-light: #ffffff;
  }
  * { margin: 0; padding: 0; box-sizing: border-box; }
  html, body {
    width: 1200px; height: 960px; overflow: hidden;
    background: var(--backdrop);
    font-family: "Open Sans", Arial, sans-serif;
  }
  .stage { position: relative; width: 1200px; height: 960px; }
  .card {
    position: absolute;
    width: 600px; height: 343px;
    overflow: hidden;
  }
  .card-front { left: 322px; top: 108px; background: var(--paper); }
  .card-back  { left: 320px; top: 493px; background: var(--brand-blue); }

  .brand-name {
    position: absolute; left: 0; right: 0; top: 88px;
    text-align: center;
    font-family: "Cinzel", Georgia, serif;
    font-weight: 500; font-size: 44px; letter-spacing: 0.02em;
    color: var(--brand-blue);
  }

  .contact-band { position: absolute; left: 0; top: 215px; width: 600px; height: 128px; }
  .contact-band svg { position: absolute; inset: 0; }

  .identity { position: absolute; left: 29px; top: 18px; color: var(--ink-light); }
  .identity .person-name { font-size: 19px; font-weight: 700; line-height: 24px; }
  .identity .job-title { font-size: 15px; font-weight: 600; line-height: 20px; margin-bottom: 2px; }
  .identity .address { font-size: 14px; font-weight: 400; line-height: 20px; }

  .contact-list {
    position: absolute; right: 30px; top: 28px;
    list-style: none; color: var(--ink-light);
    font-size: 14px; line-height: 19px; text-align: right;
  }
  .contact-list li { display: flex; justify-content: flex-end; align-items: center; gap: 6px; }
  .contact-icon { width: 14px; height: 12px; flex: none; }
  .contact-icon.plain-square { width: 11px; height: 11px; margin: 0 1px 0 2px; background: var(--ink-light); }

  .back-name {
    position: absolute; left: 0; right: 0; top: 136px;
    text-align: center;
    font-family: "Cinzel", Georgia, serif;
    font-weight: 500; font-size: 58px;
    color: var(--ink-light);
  }
  .website {
    position: absolute; left: 0; right: 0; top: 293px;
    text-align: center;
    font-size: 14px; letter-spacing: 0.45em;
    color: var(--ink-light);
  }
</style>
</head>
<body>
<div class="stage">

  <section class="card card-front">
    <div class="brand-name">Ledgerpeak</div>

    <div class="contact-band">
      <svg width="600" height="128" viewBox="0 0 600 128">
        <rect width="600" height="128" fill="var(--brand-blue)"/>
        <polygon points="0,0 264,0 349,128 0,128" fill="var(--slate)"/>
        <line x1="266" y1="0" x2="352" y2="128" stroke="var(--divider)" stroke-width="2"/>
      </svg>

      <div class="identity">
        <div class="person-name">MARK DUNN</div>
        <div class="job-title">CEO/TECHNICAL DIRECTOR</div>
        <div class="address">Suite 512, 208-3375<br>Harwood Lane NW</div>
      </div>

      <ul class="contact-list">
        <li>(587)430-9158
          <svg class="contact-icon" viewBox="0 0 14 12"><path d="M1 3.5 Q7 0 13 3.5 L12 5.5 L9.5 4.5 L9 3.5 Q7 2.8 5 3.5 L4.5 4.5 L2 5.5 Z M3 6 H11 L12.5 11.5 H1.5 Z" fill="#fff"/><circle cx="7" cy="8.5" r="1.6" fill="var(--brand-blue)"/></svg>
        </li>
        <li>mdunn@ledgerpeak.example
          <svg class="contact-icon" viewBox="0 0 14 12"><rect x="1" y="2" width="12" height="8.5" fill="#fff"/><path d="M1 2.5 L7 7 L13 2.5" stroke="var(--brand-blue)" stroke-width="1.2" fill="none"/></svg>
        </li>
        <li>@LedgerPeakYYC <span class="contact-icon plain-square"></span></li>
        <li>ledgerpeakyyc <span class="contact-icon plain-square"></span></li>
      </ul>
    </div>
  </section>

  <section class="card card-back">
    <div class="back-name">Ledgerpeak</div>
    <div class="website">www.ledgerpeak.example</div>
  </section>

</div>
</body>
</html>
```